Business Card Design of an established Waste Management, Plastic Recycling and Renewable Energy Comp

We are looking for business card design for plastic card with holograms (Very similar to credit card). I will provide our logo (Quillbys). So the name on the business card will be our logo )Quillbys) + Environmental next to it, so it will read Quillbys Environmental. The font for Environmental does not to be the same as the font of the logo. The holograms will be used to display ISO14001 Certified (In normal credit card, normally on the holograms, they show orbis or plex). I will post the design requirements from the card printing company very shortly to make sure they can use the design for the plastic card.

Target Market(s)

Companies, Government Organizations, Corporations.

Industry/Entity Type

Business

Contact Information for Business Card

Motto (Under the logo): Clean Work Always
Name: Bertolomeus Kesslani; Position: Business Manager; Address: Fernwick Landfill & Recycling Facility, Tallowmere Rd, Kelby Heights, WA 6190; Ph: +61 8 6100 4213; Mob: +61 400 917 358; E: Bertram@quillbysenvironmental.com

Requirements
Must have
• Business Names: Quillbys Logo + Environmental word after the logo.
• Motto (Under the logo): Clean Work Always
• All the Business Card Details above.
• Hologram Logo on the lower right corner which says: ISO 14001 Certified.
• Please remember the design will be printed on plastic card Not paper. The plastic crad is the same as credit card. Hope this helps. Thank You

```html
<!DOCTYPE html>
<html lang="en">
<head>
<meta charset="utf-8">
<title>Quillbys Environmental – Business Card</title>
<link href="https://fonts.googleapis.com/css2?family=Source+Sans+3:wght@400;600;700&display=swap" rel="stylesheet">
<style>
  :root {
    --stage: #161616;
    --card-white: #ffffff;
    --brand-blue: #2396d8;
    --card-blue: #2f95d6;
    --name-blue: #1f4f93;
    --ink-grey: #4a4a4a;
    --logo-grey: #55575b;
    --line-light: rgba(255, 255, 255, 0.85);
    --font-text: "Source Sans 3", "Myriad Pro", Arial, sans-serif;
  }
  * { box-sizing: border-box; margin: 0; padding: 0; }
  html, body {
    width: 1200px; height: 900px; overflow: hidden;
    background: var(--stage);
    font-family: var(--font-text);
  }
  .canvas { position: relative; width: 1200px; height: 900px; }

  .card {
    position: absolute; top: 170px;
    width: 347px; height: 561px;
  }
  .card--front { left: 259px; background: var(--card-white); }
  .card--back  { left: 631px; background: var(--card-blue); }

  .accent-tab {
    position: absolute; left: 102px;
    width: 143px; height: 30px;
    background: var(--brand-blue);
  }
  .accent-tab--top { top: 0; }
  .accent-tab--bottom { bottom: 0; height: 28px; }

  .brand {
    position: absolute; top: 112px; left: 38px;
    display: flex; align-items: center; gap: 12px;
  }
  .brand__mark {
    width: 64px; height: 64px; border-radius: 50%;
    background: var(--brand-blue); flex: none;
  }
  .brand__name {
    font-weight: 700; color: var(--logo-grey);
    font-size: 29px; line-height: 29px;
  }
  .brand__motto {
    position: absolute; top: 172px; left: 121px;
    font-size: 12px; line-height: 14px;
    color: var(--ink-grey);
  }

  .person {
    position: absolute; top: 230px; left: 0; width: 100%;
    text-align: center;
  }
  .person__name { font-size: 21px; font-weight: 700; color: var(--name-blue); line-height: 26px; }
  .person__role { font-size: 16px; color: var(--ink-grey); line-height: 20px; }

  .contact {
    position: absolute; top: 301px; left: 0; width: 100%;
    list-style: none; text-align: center;
    font-size: 16px; color: var(--ink-grey); line-height: 23.5px;
  }
  .contact__icon {
    display: inline-block; width: 12px; height: 12px;
    margin-right: 5px; vertical-align: -1px; fill: var(--name-blue);
  }

  .address {
    position: absolute; top: 398px; left: 0; width: 100%;
    text-align: center; font-style: normal;
    font-size: 16px; color: var(--ink-grey); line-height: 20.5px;
  }

  .back-emblem {
    position: absolute; top: 88px; left: 42px;
    width: 262px; height: 262px; border-radius: 50%;
    border: 2px solid rgba(255, 255, 255, 0.22);
  }
  .certificate-badge {
    position: absolute; top: 403px; left: 131px;
    width: 86px; height: 70px; border-radius: 6px;
    border: 2px solid var(--line-light);
    display: flex; align-items: center; justify-content: center;
  }
  .certificate-badge__seal {
    width: 46px; height: 46px; border-radius: 50%;
    border: 2px solid var(--line-light);
  }
</style>
</head>
<body>
<main class="canvas">

  <section class="card card--front" aria-label="Business card front">
    <div class="accent-tab accent-tab--top"></div>

    <div class="brand">
      <span class="brand__mark"></span>
      <span class="brand__name">Quillbys<br>Environmental</span>
    </div>
    <p class="brand__motto">Clean Work Always</p>

    <div class="person">
      <h1 class="person__name">Bertolomeus Kesslani</h1>
      <p class="person__role">Business Manager</p>
    </div>

    <ul class="contact">
      <li>
        <svg class="contact__icon" viewBox="0 0 24 24" aria-hidden="true"><path d="M6.6 10.8a15.1 15.1 0 0 0 6.6 6.6l2.2-2.2a1 1 0 0 1 1-.25 11.4 11.4 0 0 0 3.6.57 1 1 0 0 1 1 1V20a1 1 0 0 1-1 1A17 17 0 0 1 3 4a1 1 0 0 1 1-1h3.5a1 1 0 0 1 1 1c0 1.250.2 2.45.57 3.57a1 1 0 0 1-.25 1z"/></svg>+61 8 6100 4213
      </li>
      <li>
        <svg class="contact__icon" viewBox="0 0 24 24" aria-hidden="true"><path d="M7 1h10a2 2 0 0 1 2 2v18a2 2 0 0 1-2 2H7a2 2 0 0 1-2-2V3a2 2 0 0 1 2-2zm0 3v14h10V4zm5 15.5a1.2 1.2 0 1 0 0 2.4 1.2 1.2 0 0 0 0-2.4z"/></svg>+61 400 917 358
      </li>
      <li>
        <svg class="contact__icon" viewBox="0 0 24 24" aria-hidden="true"><path d="M2 5h20v14H2zm2 2v.5l8 5 8-5V7l-8 5z"/></svg>Bertram@quillbysenvironmental.com
      </li>
    </ul>

    <address class="address">
      Fernwick Landfill &amp; Recycling<br>
      Facility Tallowmere Rd, Kelby<br>
      Heights, WA 6190
    </address>

    <div class="accent-tab accent-tab--bottom"></div>
  </section>

  <section class="card card--back" aria-label="Business card back">
    <div class="back-emblem" aria-hidden="true"></div>
    <div class="certificate-badge" aria-label="Certification hologram">
      <span class="certificate-badge__seal"></span>
    </div>
  </section>

</main>
</body>
</html>
```